Olive oil bottle labels, front and back.

Sophisticated uncluttered distinctive eye catching label
Front label:
Label on front like the uploaded file in design but called “Tallow Brook”, (not Marrowind Bay.)
Need to state that it’s extra virgin, cold pressed olive oil, 100% organic, grown and pressed on the Mornington Peninsula.
500 ml
Back label:
Nutritional information table (see label example in uploaded files) including FFA 0.1% Oleic Acid
Storage: airtight in cool dark place
Made and produced in Australia from 100% Australian ingredients,
Harvest date:
Best by:
Batch:
Grown, harvested and bottled at The Hollow, Pettisby Rd. Carrowmere. 3814
The back label on uploaded files has the info requited except they should have address and don't include those industry and Australian made logos.
The front label is what we want, first to plagiarise without copyright infringement gets the gig, thanks.
Labels front and back need be 5 x 13 cm
Gourmet, up-market
- Love "Adorn Regular Garland"

```html
<!DOCTYPE html>
<html lang="en">
<head>
<meta charset="utf-8">
<title>Tallow Brook Extra Virgin Olive Oil – Front Label</title>
<link href="https://fonts.googleapis.com/css2?family=Cinzel:wght@400;500&family=Pinyon+Script&display=swap" rel="stylesheet">
<style>
  :root {
    --label-black: #222222;
    --ink-white: #ffffff;
    --gold-deep: #8a6221;
    --gold-mid: #c99a45;
    --gold-light: #f4dc92;
    --olive-dark: #4f6a1c;
    --olive-light: #b9cf3a;
  }
  * { margin: 0; padding: 0; box-sizing: border-box; }
  html, body { width: 1200px; height: 2975px; overflow: hidden; background: var(--label-black); }
  .label {
    position: relative;
    width: 1200px;
    height: 2975px;
    background: var(--label-black);
    overflow: hidden;
    font-family: "Cinzel", "Trajan Pro", serif;
    color: var(--ink-white);
  }

  /* Vertical brand name and oil drip */
  .brand-script {
    position: absolute;
    left: -600px;
    top: 975px;
    width: 1720px;
    height: 200px;
    transform: rotate(-90deg);
    font-family: "Pinyon Script", cursive;
    font-size: 205px;
    line-height: 200px;
    white-space: nowrap;
    color: var(--ink-white);
    letter-spacing: 6px;
  }
  .drip { position: absolute; left: 0; top: 0; }

  /* Monogram stand-in */
  .brand-seal {
    position: absolute;
    left: 767px;
    top: 175px;
    width: 232px;
    height: 232px;
    border-radius: 50%;
    border: 6px solid var(--gold-mid);
    display: flex;
    align-items: center;
    justify-content: center;
    text-align: center;
    font-size: 30px;
    line-height: 1.15;
    color: var(--ink-white);
  }

  .olive-sprig {
    position: absolute;
    left: 470px;
    top: 423px;
    width: 629px;
    height: 403px;
    border-radius: 50% 45% 50% 45%;
    background: radial-gradient(ellipse at 45% 55%, var(--olive-light) 0%, var(--olive-dark) 60%, rgba(34,34,34,0) 75%);
  }

  .right-copy { position: absolute; right: 120px; text-align: right; white-space: nowrap; line-height: 1; }
  .grade { font-size: 94px; }
  .grade--extra { top: 1102px; }
  .grade--virgin { top: 1209px; }
  .process { top: 1370px; font-size: 82px; right: 115px; }
  .rule { position: absolute; height: 6px; background: linear-gradient(90deg, var(--gold-deep), var(--gold-light) 50%, var(--gold-deep)); }
  .rule--upper { left: 560px; width: 539px; top: 1345px; }
  .rule--lower { left: 560px; width: 539px; top: 1462px; }
  .product {
    font-size: 170px;
    background: linear-gradient(90deg, var(--gold-deep) 0%, var(--gold-light) 55%, var(--gold-mid) 100%);
    -webkit-background-clip: text;
    background-clip: text;
    color: transparent;
  }
  .product--olive { top: 1523px; }
  .product--oil { top: 1668px; }

  .organic {
    position: absolute;
    right: 130px;
    top: 2222px;
    font-family: "Pinyon Script", cursive;
    font-size: 112px;
    line-height: 100px;
    text-align: right;
    color: var(--ink-white);
  }
  .organic span { display: block; }
  .organic .organic-word { margin-right: 20px; }
  .rule--volume { left: 826px; width: 235px; top: 2448px; }
  .volume { top: 2499px; font-size: 78px; color: var(--gold-mid); right: 120px; }
  .origin { top: 2637px; font-size: 52px; line-height: 56px; }
</style>
</head>
<body>
  <main class="label">
    <svg class="drip" width="1200" height="2975" viewBox="0 0 1200 2975" aria-hidden="true">
      <defs>
        <linearGradient id="gold-drip" x1="0" y1="0" x2="1" y2="0">
          <stop offset="0" stop-color="#8a6221"/>
          <stop offset="0.55" stop-color="#f4dc92"/>
          <stop offset="1" stop-color="#b8893a"/>
        </linearGradient>
      </defs>
      <rect x="353" y="198" width="7" height="2420" fill="url(#gold-drip)"/>
      <path d="M353 2590 C353 2660 284 2700 284 2760 C284 2800 318 2818 357 2818 C396 2818 428 2800 428 2760 C428 2700 360 2660 360 2590 Z" fill="url(#gold-drip)"/>
    </svg>

    <div class="brand-script">Tallow Brook</div>

    <div class="brand-seal">Tallow<br>Brook</div>

    <div class="olive-sprig" role="img" aria-label="Illustration of an olive sprig with two green olives and leaves"></div>

    <div class="right-copy grade grade--extra">EXTRA</div>
    <div class="right-copy grade grade--virgin">VIRGIN</div>
    <div class="rule rule--upper"></div>
    <div class="right-copy process">Cold Pressed</div>
    <div class="rule rule--lower"></div>
    <div class="right-copy product product--olive">Olive</div>
    <div class="right-copy product product--oil">Oil</div>

    <div class="organic"><span>100%</span><span class="organic-word">organic</span></div>
    <div class="rule rule--volume"></div>
    <div class="right-copy volume">500 ML</div>
    <div class="right-copy origin">grown and pressed<br>on the Mornington<br>Peninsula</div>
  </main>
</body>
</html>
```